Halvery Building Group Website

Need a dynamic corporate website that can be built on with time. We want to get our information out to the world and have a place where customers can submit requests for proposals.

Target Market(s)

Custom home owners and buyers. Architects and Real Estate Agents.

Industry/Entity Type

Construction

Number of Pages Required

3 page

Font styles to use
Serif
Sans Serif

Requirements
Must have
• Company logo, about, company contact information, biography, contact, projects,
• Sleek, modern, clean, attractive design.
• Online form customers can use for filling out a request for project proposal.
• Workcircle hyperlink.
• Uses www.halverybuildinggroup.example

```html
<!DOCTYPE html>
<html lang="en">
<head>
<meta charset="utf-8">
<title>Halvery Building Group</title>
<link rel="stylesheet" href="https://fonts.googleapis.com/css2?family=Michroma&family=Roboto:wght@400;500;700&family=Open+Sans:wght@400&display=swap">
<style>
  :root {
    --navy: #0b3e86;
    --blue: #1d5fae;
    --heading: #123f8f;
    --accent-line: #3f8fd8;
    --hero-dark: #15213a;
    --hero-mid: #2c4a74;
    --white: #ffffff;
    --text: #2a2a2a;
    --field-border: #9a9a9a;
    --map-light: #f6f7f3;
    --map-green: #e8eddc;
  }
  * { margin: 0; padding: 0; box-sizing: border-box; }
  html, body { width: 1200px; height: 929px; overflow: hidden; }
  body { position: relative; font-family: "Roboto", sans-serif; background: var(--white); color: var(--text); }

  .hero {
    position: absolute; left: 0; top: 0; width: 1200px; height: 533px;
    background: radial-gradient(ellipse at 55% 45%, #3b5a84 0%, var(--hero-mid) 35%, var(--hero-dark) 85%);
  }
  .hero-photo { position: absolute; inset: 0; }
  .brand {
    position: absolute; left: 99px; top: 34px; display: flex; align-items: center; gap: 12px;
  }
  .brand-square { width: 56px; height: 56px; background: var(--white); border-radius: 6px; }
  .brand-name {
    font-family: "Roboto", sans-serif; font-weight: 700; color: var(--white);
    font-size: 22px; line-height: 26px; letter-spacing: 1px; text-transform: uppercase;
  }
  .main-nav { position: absolute; top: 49px; left: 645px; display: flex; align-items: center; }
  .main-nav a {
    color: var(--white); text-decoration: none; font-weight: 500; font-size: 16px;
    padding: 8px 13px; margin-right: 12px;
  }
  .main-nav a.active { background: var(--blue); border: 1px solid #8fb8ea; border-radius: 2px; }
  .hero-title {
    position: absolute; top: 262px; left: 0; width: 1200px; text-align: center;
    font-family: "Michroma", sans-serif; color: var(--white); font-size: 40px; letter-spacing: 1px;
  }
  .hero-sub {
    position: absolute; top: 336px; left: 0; width: 1200px; text-align: center;
    color: var(--white); font-size: 26px; font-weight: 400;
  }
  .arrow { position: absolute; top: 303px; }
  .arrow.prev { left: 27px; }
  .arrow.next { left: 1140px; }

  .accent-line { position: absolute; top: 533px; left: 0; width: 1200px; height: 4px; background: var(--accent-line); }

  .info {
    position: absolute; top: 537px; left: 0; width: 1200px; height: 331px;
    background: linear-gradient(90deg, var(--map-green) 0%, var(--map-light) 40%, var(--map-light) 80%, #e6eef2 100%);
  }
  .footer-brand {
    position: absolute; left: 99px; top: 105px; width: 240px; display: flex; align-items: center; gap: 10px;
  }
  .footer-brand .brand-square { width: 40px; height: 40px; background: var(--blue); }
  .footer-brand .brand-name { color: var(--heading); font-size: 22px; line-height: 27px; }

  .col-title {
    position: absolute; top: 44px; font-weight: 700; color: var(--heading); font-size: 21px;
  }
  .col-title::after {
    content: ""; position: absolute; left: 0; top: 36px; width: 104px; height: 2px; background: var(--heading);
  }
  .quick-links { position: absolute; left: 385px; top: 106px; list-style: none; }
  .quick-links li { font-size: 16px; height: 32px; color: var(--text); }
  .quick-links li::before { content: "›"; margin-right: 7px; }

  .contact-item { position: absolute; left: 549px; display: flex; gap: 18px; }
  .contact-icon {
    width: 38px; height: 38px; border: 2px solid var(--heading); border-radius: 50%;
    display: flex; align-items: center; justify-content: center; flex-shrink: 0;
  }
  .contact-item h4 { font-size: 15px; font-weight: 500; color: var(--text); margin-bottom: 4px; }
  .contact-item p { font-size: 13.5px; line-height: 21px; }
  .contact-item .label { font-size: 16px; font-weight: 400; }

  .rfp-form { position: absolute; left: 814px; top: 100px; width: 286px; }
  .field {
    position: absolute; border: 1px solid var(--field-border); border-radius: 3px; background: var(--white);
    font-family: "Open Sans", sans-serif; font-size: 12px; color: #333; padding: 11px 12px;
  }
  .send-btn {
    position: absolute; left: 0; top: 123px; width: 118px; height: 38px; background: var(--navy);
    color: var(--white); font-weight: 500; font-size: 14px; border: none; border-radius: 3px;
    display: flex; align-items: center; justify-content: center;
  }

  .bottom-bar { position: absolute; top: 868px; left: 0; width: 1200px; height: 61px; background: var(--navy); }
  .copyright { position: absolute; left: 98px; top: 20px; color: var(--white); font-size: 15px; }
  .social { position: absolute; left: 949px; top: 13px; display: flex; gap: 6px; }
  .social span {
    width: 34px; height: 34px; border: 2px solid var(--white); border-radius: 50%;
    color: var(--white); font-size: 11px; font-weight: 500; display: flex; align-items: center; justify-content: center;
  }
</style>
</head>
<body>
  <header class="hero">
    <div class="hero-photo" role="img" aria-label="Night view looking up at a building under construction with a tower crane and glass towers"></div>
    <div class="brand">
      <div class="brand-square"></div>
      <div class="brand-name">Halvery<br>Building Group, Inc.</div>
    </div>
    <nav class="main-nav">
      <a class="active">HOME</a><a>ABOUT</a><a>BIO</a><a>PROJECTS</a><a>CONTACT US</a>
    </nav>
    <h1 class="hero-title">HALVERY BUILDING GROUP</h1>
    <p class="hero-sub">Commercial, Residential and Community Solutions</p>
    <svg class="arrow prev" width="32" height="56" viewBox="0 0 32 56"><polyline points="30,2 3,28 30,54" fill="none" stroke="#fff" stroke-width="2"/></svg>
    <svg class="arrow next" width="32" height="56" viewBox="0 0 32 56"><polyline points="2,2 29,28 2,54" fill="none" stroke="#fff" stroke-width="2"/></svg>
  </header>

  <div class="accent-line"></div>

  <section class="info" role="img" aria-label="Faint map of Australia behind the contact details">
    <div class="footer-brand">
      <div class="brand-square"></div>
      <div class="brand-name">Halvery<br>Building Group, Inc.</div>
    </div>

    <h3 class="col-title" style="left:385px">QUICK LINKS</h3>
    <ul class="quick-links">
      <li>Home</li><li>About</li><li>Bio</li><li>Projects</li><li>Contact Us</li>
    </ul>

    <h3 class="col-title" style="left:548px">CONTACT US</h3>
    <div class="contact-item" style="top:106px">
      <div class="contact-icon"><svg width="14" height="18" viewBox="0 0 14 18"><path d="M7 1a6 6 0 0 0-6 6c0 4.5 6 10 6 10s6-5.5 6-10a6 6 0 0 0-6-6z" fill="none" stroke="#123f8f" stroke-width="2"/><circle cx="7" cy="7" r="2" fill="#123f8f"/></svg></div>
      <div><h4>HALVERY BUILDING,</h4><p>Marlow Ridge, West<br>ern Australia, 6099.</p></div>
    </div>
    <div class="contact-item" style="top:183px">
      <div class="contact-icon"><svg width="10" height="16" viewBox="0 0 10 16"><rect x="1" y="1" width="8" height="14" rx="1.5" fill="none" stroke="#123f8f" stroke-width="2"/><rect x="3" y="11" width="4" height="1.5" fill="#123f8f"/></svg></div>
      <div><h4 class="label">PHONE:</h4><p>1800 0000 4417</p></div>
    </div>
    <div class="contact-item" style="top:244px">
      <div class="contact-icon"><svg width="14" height="11" viewBox="0 0 14 11"><rect x="0" y="0" width="14" height="11" rx="1.5" fill="#123f8f"/><polyline points="1,1.5 7,6 13,1.5" fill="none" stroke="#fff" stroke-width="1.4"/></svg></div>
      <div><h4 class="label">Mail:</h4><p>info@halverybuilding<br>group.example</p></div>
    </div>

    <h3 class="col-title" style="left:814px">CONTACT FORM</h3>
    <form class="rfp-form">
      <div class="field" style="left:0;top:0;width:137px;height:35px">Name</div>
      <div class="field" style="left:148px;top:0;width:138px;height:35px">Phone</div>
      <div class="field" style="left:0;top:43px;width:286px;height:64px">Message</div>
      <div class="send-btn">SEND MESSAGE</div>
    </form>
  </section>

  <footer class="bottom-bar">
    <p class="copyright">Copyright © 2016 Halvery Building Group. All Right Reserved</p>
    <div class="social">
      <span title="Workcircle">Wc</span><span title="Pinnly">Pn</span><span title="Chirpa">Ch</span><span title="Gplex">Gx</span>
    </div>
  </footer>
</body>
</html>
```